Business school needs a web design

Who We are:
KRVT is a small business school that offers programs in Project Management. The school is based in West Africa and welcomes students from the whole area. Our aim is to become one of the reference business schools in Africa.

Project Brief:
The site will include all informations relevant for different types of visitors that we have: actual and future students, companies, mass media, future employees, ect. It will present information about subscription, list of programs, presentation of the school and its team,etc.

What We want:
This competition is for Design only no coding! We need design for two pages.
We did some wireframing for the home page and the list of programs page. We made them just to show how we imagine the website would look like. But we encourage creative designs, so you don't have to stick to the wireframe models.

Sites We like:
http://www.ravenmoorcollege.example/
http://www.belvantis.example/fr/etudes.html
http://www.qtl.example/mba/Pages/default.aspx

Color schemes
The logo of the school is red and black. So the color scheme of the website should match that. For the rest, it is opened to your imagination.
Updates

The payment for the project is now garanteed. Good luck to you all !

Target Market(s)

The target market is diversified because we have students of different ages, also company representatives or employees that might visit the website for recruitment purposes. But the majority of our audience should be aged between 20 - 30 years.

Industry/Entity Type

Small Business

Requirements
Must have
• The design must include two pages: a home page and another interior page : might be the list of programs or any other page relevant to the domain. The Home page must include a slide show at the beginning.
The background page must be white.
Nice to have
• The use of flat design for this project is preferred.
The use of Pelican scaffold as a base for the design is an asset.

```html
<!DOCTYPE html>
<html lang="fr">
<head>
<meta charset="utf-8">
<title>KRVT – Programmes et Formations</title>
<link rel="stylesheet" href="https://fonts.googleapis.com/css2?family=Roboto+Condensed:wght@400;700&family=Open+Sans:wght@400;600;700&display=swap">
<style>
:root{
  --red:#c8161d;
  --red-dark:#9e0f14;
  --red-light:#e0262d;
  --ink:#222;
  --grey:#6b6b6b;
  --line:#dcdcdc;
  --band:#ececec;
  --footer:#141414;
  --white:#fff;
}
*{box-sizing:border-box;margin:0;padding:0}
html,body{width:677px;height:1200px;overflow:hidden;background:var(--white)}
body{position:relative;font-family:"Open Sans",Arial,sans-serif;color:var(--ink)}
.abs{position:absolute}

.utility-bar{left:293px;top:0;width:363px;height:27px;background:#f4f4f4;border-radius:0 0 6px 6px;box-shadow:0 1px 3px rgba(0,0,0,.18);display:flex;align-items:center;justify-content:center;gap:6px;font:700 10.5px "Open Sans",sans-serif}
.utility-bar a{color:var(--ink);text-decoration:none}
.utility-bar a.current{color:var(--red)}
.utility-bar .sep{color:#999}

.brand{left:23px;top:22px;display:flex;align-items:center;gap:8px}
.brand-mark{width:22px;height:22px;background:var(--ink)}
.brand-name{font:700 34px "Roboto Condensed",sans-serif;color:var(--red);letter-spacing:1px}

.search{left:417px;top:51px;width:228px;height:18px;border:1px solid #cfcfcf;border-radius:9px;background:#fafafa;display:flex;align-items:center;padding:0 8px;font:700 9px "Open Sans",sans-serif;color:#555}
.search svg{margin-left:auto}

.main-nav{left:23px;top:107px;width:624px;height:32px;background:linear-gradient(#d8222a,var(--red-dark));border-radius:3px;display:flex;box-shadow:0 2px 3px rgba(0,0,0,.2)}
.main-nav a{color:var(--white);text-decoration:none;font:700 13px "Roboto Condensed",sans-serif;display:flex;align-items:center;padding:0 17px;border-right:1px solid rgba(0,0,0,.25)}
.main-nav a:last-child{border-right:none}

.hero{left:23px;top:145px;width:624px;height:242px;border-radius:4px;overflow:hidden}
.hero-photo{position:absolute;inset:0;background:linear-gradient(100deg,#c9b79a 0%,#e7dccb 35%,#bfc6c8 65%,#8fa39d 100%)}
.hero-panel{position:absolute;left:0;top:0}
.hero-copy{position:absolute;left:32px;top:50px;color:var(--white)}
.hero-kicker{font:700 19px "Roboto Condensed",sans-serif}
.hero-title{font:700 38px/38px "Roboto Condensed",sans-serif;margin-top:2px}
.hero-btn{display:inline-block;margin-top:12px;border:1.5px solid var(--white);padding:3px 12px;font:700 14px "Roboto Condensed",sans-serif;color:var(--white)}

.breadcrumb{left:23px;top:393px;font:600 9.5px "Open Sans",sans-serif;color:var(--ink)}
.breadcrumb a{color:var(--red);text-decoration:none}
.crumb-band{left:0;top:410px;width:677px;height:4px;background:linear-gradient(#e6e6e6,#fff)}

.page-title{left:0;top:430px;width:677px;text-align:center;font:700 19px "Roboto Condensed",sans-serif;color:var(--red);letter-spacing:1px;word-spacing:6px}
.title-rule{left:220px;top:460px;width:237px;height:1px;background:var(--line)}
.intro{left:60px;top:471px;width:557px;text-align:center;font:400 10px/14px "Open Sans",sans-serif;color:var(--grey)}

.video-box{left:23px;top:544px;width:624px;height:240px;border:1px solid var(--line);box-shadow:0 0 4px rgba(0,0,0,.12);background:var(--white)}
.video{left:33px;top:555px;width:403px;height:218px;background:linear-gradient(120deg,#8b7c6d,#c2b5a5 50%,#5f6a70);}
.player-bar{left:33px;top:753px;width:403px;height:20px;background:#1b1b1b}
.progress{left:40px;top:757px;width:389px;height:3px;background:#555}
.progress span{display:block;width:37%;height:100%;background:var(--red)}
.player-bar-text{left:84px;top:762px;font:400 7px "Open Sans",sans-serif;color:#ccc}
.play{left:210px;top:638px}

.playlist{left:452px;top:555px;width:181px;height:218px;border:1px solid var(--line)}
.thumb{left:469px;width:134px;background:linear-gradient(120deg,#7a8a9a,#c7c0b4 55%,#6d5a4d)}
.thumb-cap{left:469px;font:400 8px "Open Sans",sans-serif;color:#2a5aa8}
.scroll{left:617px;top:562px;width:9px;height:204px;background:#eee;border-radius:4px}
.scroll span{display:block;margin:2px;height:40px;background:#bbb;border-radius:3px}

.section-rule{left:23px;top:813px;width:624px;height:1px;background:var(--line)}
.section-title{left:23px;top:830px;font:700 15px "Roboto Condensed",sans-serif;color:var(--red);letter-spacing:1px;word-spacing:5px}

.card{width:143px;height:87px;top:860px;border:1px solid var(--line);padding:4px;background:var(--white);box-shadow:0 1px 3px rgba(0,0,0,.1)}
.card div{width:100%;height:100%}
.card-label{top:953px;font:600 11px "Open Sans",sans-serif;color:var(--ink)}

.partners{left:0;top:987px;width:677px;height:44px;background:#f0f0f0;border-top:1px solid #e2e2e2}
.partner{top:996px;height:26px;border-radius:3px}
.arrow-btn{top:1001px;width:16px;height:16px;border-radius:50%;background:#bdbdbd}

.footer{left:0;top:1033px;width:677px;height:167px;background:linear-gradient(#262626,var(--footer))}
.f-col{top:1049px;font:400 7.5px/12px "Open Sans",sans-serif;color:#ddd}
.f-col h3{font:700 10.5px "Roboto Condensed",sans-serif;color:var(--red);margin-bottom:6px}
.socials{display:flex;gap:4px;margin-top:4px}
.socials span{width:16px;height:16px;background:#3b6fb6}
.socials span:nth-child(3){background:var(--red)}
.contact-line{display:flex;align-items:center;gap:5px;margin-top:6px}
.email-field{width:134px;height:14px;background:var(--white);margin-top:6px;font-size:6.5px;color:#888;padding:2px 4px;line-height:10px}
.subscribe{display:inline-block;background:var(--red);color:var(--white);font:700 7.5px "Open Sans",sans-serif;padding:2px 8px;margin-top:5px}
.footer-rule{left:23px;top:1175px;width:624px;height:1px;background:#444}
.copyright{left:23px;top:1181px;font:400 7.5px "Open Sans",sans-serif;color:#ccc}
</style>
</head>
<body>

<nav class="utility-bar abs">
  <a class="current" href="#">Repertoire du personnel</a><span class="sep">|</span>
  <a href="#">Blogue</a><span class="sep">|</span>
  <a href="#">Salle de presse</a><span class="sep">|</span>
  <a href="#">Nous joindre</a><span class="sep">|</span>
  <a href="#">Francais</a>
</nav>

<div class="brand abs"><span class="brand-mark"></span><span class="brand-name">KRVT</span></div>

<div class="search abs">SEARCH
  <svg width="10" height="10" viewBox="0 0 10 10"><circle cx="4" cy="4" r="3" fill="none" stroke="#999" stroke-width="1.3"/><line x1="6.2" y1="6.2" x2="9" y2="9" stroke="#999" stroke-width="1.3"/></svg>
</div>

<nav class="main-nav abs">
  <a href="#">A propos de l'KRVT</a>
  <a href="#">Programmes et Formations</a>
  <a href="#">Etudiants</a>
  <a href="#">Nouvelles et Evenements</a>
  <a href="#">Entreprises</a>
</nav>

<section class="hero abs">
  <div class="hero-photo" role="img" aria-label="Groupe d'étudiants travaillant ensemble en plein air avec un ordinateur portable"></div>
  <svg class="hero-panel" width="300" height="242" viewBox="0 0 300 242">
    <defs><linearGradient id="panelGrad" x1="0" y1="0" x2="1" y2="1"><stop offset="0" stop-color="#d31d24"/><stop offset="1" stop-color="#a50f15"/></linearGradient></defs>
    <path d="M0 0 H255 C300 60 300 180 262 242 H0 Z" fill="url(#panelGrad)"/>
  </svg>
  <div class="hero-copy">
    <div class="hero-kicker">An innovative graduate</div>
    <div class="hero-title">School of<br>Business</div>
    <span class="hero-btn">MORE INFO</span>
  </div>
</section>

<div class="breadcrumb abs"><a href="#">Accueil</a> &gt; Programmes et Formations</div>
<div class="crumb-band abs"></div>

<h1 class="page-title abs">PROGRAMMES ET FORMATIONS</h1>
<div class="title-rule abs"></div>
<p class="intro abs">lorem ipsum dolor sit amet, consectetur adipisicing elit, sed do eiusmod tempor incididunt ut labore et dolore magna aliqua Ut enim ad minim veniam, quis nostrud exercitation ullamco laboris nisi ut aliquip ex ea commodo consequat. Duis aute irure dolor in reprehenderit in voluptate velit esse cillum dolore eu fugiat nulla pariatur. Excepteur sint occaecat cupidatat non proident, sunt in culpa qui officio deserunt mollit anim id est laborum.</p>

<div class="video-box abs"></div>
<div class="video abs" role="img" aria-label="Vidéo : un enseignant aide des étudiants devant des ordinateurs"></div>
<svg class="play abs" width="50" height="50" viewBox="0 0 50 50"><circle cx="25" cy="25" r="25" fill="rgba(0,0,0,.55)"/><path d="M20 15 L35 25 L20 35 Z" fill="#fff"/></svg>
<div class="player-bar abs"></div>
<div class="progress abs"><span></span></div>
<svg class="abs" style="left:40px;top:763px" width="24" height="8" viewBox="0 0 24 8"><path d="M0 0 L6 4 L0 8Z" fill="#ddd"/><rect x="12" y="1" width="2" height="6" fill="#ddd"/><path d="M15 1 L20 4 L15 7Z" fill="#ddd"/></svg>
<div class="player-bar-text abs">1:16 / 3:10</div>
<svg class="abs" style="left:372px;top:762px" width="58" height="8" viewBox="0 0 58 8"><rect x="0" y="1" width="8" height="6" fill="var(--red)"/><rect x="14" y="1" width="14" height="6" fill="#777"/><rect x="34" y="1" width="8" height="6" fill="none" stroke="#ccc"/><rect x="48" y="1" width="8" height="6" fill="none" stroke="#ccc"/></svg>

<div class="playlist abs"></div>
<div class="thumb abs" style="top:564px;height:49px" role="img" aria-label="Miniature vidéo : étudiants en classe"></div>
<div class="thumb abs" style="top:633px;height:50px" role="img" aria-label="Miniature vidéo : étudiants sur le campus"></div>
<div class="thumb-cap abs" style="top:687px">proident, sunt in culpa qui officio</div>
<div class="thumb abs" style="top:703px;height:52px" role="img" aria-label="Miniature vidéo : groupe d'étudiants souriants"></div>
<div class="thumb-cap abs" style="top:759px">proident, sunt in culpa qui officio</div>
<div class="scroll abs"><span></span></div>

<div class="section-rule abs"></div>
<h2 class="section-title abs">PROGRAMMES OFFERTS</h2>

<div class="card abs" style="left:23px"><div role="img" aria-label="Étudiante passant un test de placement" style="background:linear-gradient(120deg,#6e5a4a,#c9a98a 50%,#3e4f6a)"></div></div>
<div class="card abs" style="left:183px"><div role="img" aria-label="Enseignante devant un tableau" style="background:linear-gradient(120deg,#8a9a8a,#d8d2c2 55%,#9a7a62)"></div></div>
<div class="card abs" style="left:341px"><div role="img" aria-label="Étudiants marchant devant des drapeaux" style="background:linear-gradient(120deg,#5e7a8e,#c6b8a8 50%,#8a4a3a)"></div></div>
<div class="card abs" style="left:500px"><div role="img" aria-label="Étudiante passant un test de placement" style="background:linear-gradient(120deg,#6e5a4a,#c9a98a 50%,#3e4f6a)"></div></div>
<div class="card-label abs" style="left:25px">Placement Testing</div>
<div class="card-label abs" style="left:185px">Teacher Education</div>
<div class="card-label abs" style="left:343px">Study Abroad</div>
<div class="card-label abs" style="left:502px">Placement Testing</div>

<div class="partners abs"></div>
<div class="arrow-btn abs" style="left:25px"></div>
<svg class="abs" style="left:30px;top:1005px" width="6" height="8" viewBox="0 0 6 8"><path d="M5 0 L1 4 L5 8" fill="none" stroke="#fff" stroke-width="1.6"/></svg>
<div class="arrow-btn abs" style="left:631px"></div>
<svg class="abs" style="left:636px;top:1005px" width="6" height="8" viewBox="0 0 6 8"><path d="M1 0 L5 4 L1 8" fill="none" stroke="#fff" stroke-width="1.6"/></svg>
<div class="partner abs" style="left:64px;width:62px;background:#e0a47a"></div>
<div class="partner abs" style="left:172px;width:38px;background:#a0906a"></div>
<div class="partner abs" style="left:234px;width:46px;background:#2f7fc1"></div>
<div class="partner abs" style="left:305px;width:56px;background:#9cb6d6"></div>
<div class="partner abs" style="left:393px;width:44px;background:#8a8a8a"></div>
<div class="partner abs" style="left:459px;width:55px;background:#d88080"></div>
<div class="partner abs" style="left:535px;width:56px;background:#9cb6d6"></div>

<footer class="footer abs"></footer>
<div class="f-col abs" style="left:23px">
  <h3>Suivez-nous</h3>
  <div class="socials"><span></span><span></span><span></span><span></span></div>
</div>
<div class="f-col abs" style="left:149px;width:100px">
  <h3>A propos</h3>
  A propos de l'KRVT Admissions Calendrier de l'école Offres d'emploi Repertoire du personnel
</div>
<div class="f-col abs" style="left:273px;width:90px">
  <h3>Etudiants</h3>
  Accueil étudiants<br>Vie étudiante<br>Entreprises<br>Blogue<br>Étudiants J For<br>Formations
</div>
<div class="f-col abs" style="left:381px;width:105px">
  <h3>KRVT</h3>
  14, RUE DES BAOBABS<br>Ancienne route, près du Marché Central
  <div class="contact-line"><svg width="7" height="9" viewBox="0 0 7 9"><path d="M1 0 H3 L3 3 L2 4 C2.5 5.5 3.5 6.5 4.5 7 L5.5 6 L7 7 V9 C3 9 0 6 0 1Z" fill="var(--red)"/></svg>(221) 30 412 77 19</div>
  <div class="contact-line"><svg width="7" height="9" viewBox="0 0 7 9"><path d="M1 0 H3 L3 3 L2 4 C2.5 5.5 3.5 6.5 4.5 7 L5.5 6 L7 7 V9 C3 9 0 6 0 1Z" fill="var(--red)"/></svg>(221) 70 555 21 48</div>
</div>
<div class="f-col abs" style="left:511px;width:140px">
  <h3>Infolettre <svg width="16" height="11" viewBox="0 0 16 11" style="vertical-align:-1px;margin-left:6px"><rect width="16" height="11" fill="var(--red)"/><path d="M0 0 L8 6 L16 0" fill="none" stroke="#fff" stroke-width="1"/></svg></h3>
  Créée pour former des professionnels de haut niveau capables de planifier et de réaliser des projets
  <div class="email-field">Enter Your Email...</div>
  <span class="subscribe">Subscribe</span>
</div>
<div class="footer-rule abs"></div>
<div class="copyright abs">©KRVT, 2013 Tous droits reserves</div>

</body>
</html>
```